Breakfast Cafe - The Coral Table

It is for my breakfast and lunch cafe with a hawaiian / beach theme. I am open 7 days a week from 7am to 2pm. We serve traditional American food such as omelettes, pancakes, burgers and sandwiches. I'll upload my old card and my new logo to be used. We have a lot of day to day regulars who eat there during the week, our t-shirts actually say 'Locals Only' on them. Hope this helps. Thanks.

Target Market(s)

anyone who has an appetite!

Industry/Entity Type

American Restaurant

Contact Information for Business Card

4815C Driftwood Shore Road
Long Beach, California
(562) 555-0187

Requirements
Must have
• Address and phone number easily readable.
Nice to have
• beach or tropical theme

```html
<!DOCTYPE html>
<html lang="en">
<head>
<meta charset="utf-8">
<title>The Coral Table – Business Card</title>
<link rel="stylesheet" href="https://fonts.googleapis.com/css2?family=Oswald:wght@500;600&display=swap">
<style>
  :root {
    --paper: #ffffff;
    --sun: #f5a13a;
    --bark: #a8521c;
    --foam: #e6f6f8;
    --shallow: #5fd0d8;
    --lagoon: #1fa6c4;
    --deep: #137a9a;
    --ink-light: #ffffff;
  }
  html, body {
    margin: 0;
    padding: 0;
    overflow: hidden;
    background: var(--paper);
  }
  .card {
    position: relative;
    width: 720px;
    height: 1200px;
    overflow: hidden;
    background: var(--paper);
    font-family: "Oswald", "Arial Narrow", sans-serif;
  }
  .brand {
    position: absolute;
    top: 0;
    left: 0;
    width: 720px;
    text-align: center;
  }
  .brand-disc {
    display: block;
    width: 300px;
    height: 300px;
    margin: 128px auto 0;
    border-radius: 50%;
    background: var(--sun);
  }
  .brand-name {
    margin: 18px 0 0;
    font-size: 66px;
    font-weight: 600;
    line-height: 1;
    letter-spacing: 1px;
    color: var(--bark);
  }
  .ocean {
    position: absolute;
    left: 0;
    top: 0;
    width: 720px;
    height: 1200px;
  }
  .contact {
    position: absolute;
    left: 0;
    top: 780px;
    width: 720px;
    text-align: center;
    color: var(--ink-light);
  }
  .contact-address,
  .contact-phone {
    margin: 0;
    font-size: 39px;
    font-weight: 600;
    line-height: 1.2;
  }
  .contact-tagline {
    margin: 22px 0 0;
    font-size: 22px;
    font-weight: 500;
  }
  .contact-hours {
    margin: 30px 0 0;
    font-size: 22px;
    font-weight: 500;
  }
</style>
</head>
<body>
  <main class="card">
    <header class="brand">
      <span class="brand-disc" aria-hidden="true"></span>
      <h1 class="brand-name">The Coral Table</h1>
    </header>

    <svg class="ocean" viewBox="0 0 720 1200" role="img" aria-label="Aerial photograph of turquoise ocean water with white surf breaking across the top">
      <defs>
        <linearGradient id="sea" x1="1" y1="0" x2="0" y2="1">
          <stop offset="0" stop-color="var(--foam)"/>
          <stop offset="0.22" stop-color="var(--shallow)"/>
          <stop offset="0.55" stop-color="var(--lagoon)"/>
          <stop offset="1" stop-color="var(--deep)"/>
        </linearGradient>
      </defs>
      <path d="M0,672 A612,612 0 0 1 720,672 L720,1200 L0,1200 Z" fill="url(#sea)"/>
    </svg>

    <section class="contact">
      <p class="contact-address">4815C Driftwood Shore Road<br>Long Beach, California</p>
      <p class="contact-phone">(562) 555-0187</p>
      <p class="contact-tagline">family owned and operated!</p>
      <p class="contact-hours">BREAKFAST AND LUNCH 7am-2pm daily</p>
    </section>
  </main>
</body>
</html>
```